New Business Card Needed

I need a new business card for Willowmere Kitchen & Bath.
Logo is attached as well a my photo. Note: Make the logo Navy Blue.
Here is the text:
Desmond Ferrick
GC/Owner
Larkfield NC
704-555-0183
desmond@willowmereKB.example
www.willowmereKB.example
Tag line on card: BEAUTY | FUNCTION | ON TIME | ON BUDGET
Trim size: 2.56" X 2.56"
This is where we aim to cut the cards.
Safe area: 2.4" X 2.4"
Make sure any important aspects of your design such as text and logos are inside of the safe area, otherwise they may be cut off.
Bleed area: 2.71 X 2.71
Make sure that your background extends to fill the bleed to avoid your Business Cards having white edges when trimmed.
On the back side. Use photo of kitchen attached.

```html
<!DOCTYPE html>
<html lang="en">
<head>
<meta charset="utf-8">
<title>Willowmere Kitchen &amp; Bath — Business Card</title>
<link rel="stylesheet" href="https://fonts.googleapis.com/css2?family=Lato:wght@400;700;900&display=swap">
<style>
  :root {
    --navy: #13204a;
    --ink: #1c2235;
    --white: #ffffff;
    --stage: #2b2d31;
    --wood-light: #d9b98c;
    --counter: #ecebe7;
    --portrait-1: #e4e2e0;
    --portrait-2: #3d4660;
  }
  * { box-sizing: border-box; margin: 0; padding: 0; }
  html, body {
    width: 1200px; height: 904px; overflow: hidden;
    background: var(--stage);
    font-family: "Lato", sans-serif;
  }
  .canvas { position: relative; width: 1200px; height: 904px; }

  .card {
    position: absolute;
    width: 680px; height: 389px;
    overflow: hidden;
    box-shadow: 0 14px 30px rgba(0,0,0,.45);
  }

  /* back side */
  .card--back { left: 90px; top: 46px; }
  .kitchen-photo {
    width: 100%; height: 100%;
    background: linear-gradient(160deg, var(--counter) 0%, #d8d2c8 40%, var(--wood-light) 75%, #a9784f 100%);
  }

  /* front side */
  .card--front { left: 430px; top: 468px; background: var(--white); }
  .portrait {
    position: absolute; right: 0; top: 0;
    width: 320px; height: 339px;
    background: linear-gradient(180deg, var(--portrait-1) 0%, #b9b3ae 55%, var(--portrait-2) 100%);
  }
  .tagline-band {
    position: absolute; left: 0; right: 0; bottom: 0;
    height: 50px; background: var(--navy);
    display: flex; align-items: center; justify-content: flex-end;
    padding-right: 34px;
    color: var(--white);
    font-weight: 700; font-size: 22px; letter-spacing: .5px;
  }
  .tagline-band .sep { margin: 0 8px; font-weight: 400; }

  .brand { position: absolute; left: 58px; top: 38px; }
  .brand-name {
    color: var(--navy); font-weight: 700; font-size: 19px; letter-spacing: 1.5px;
    text-transform: uppercase; line-height: 1.15;
  }

  .identity { position: absolute; left: 58px; top: 112px; color: var(--navy); }
  .person-name { font-weight: 900; font-size: 26px; }
  .person-role { margin-top: 4px; font-size: 16px; color: var(--ink); }

  .contacts { position: absolute; left: 58px; top: 186px; list-style: none; color: var(--ink); }
  .contacts li { display: flex; align-items: center; gap: 12px; font-size: 17px; height: 28px; }
  .contacts svg { width: 18px; height: 18px; fill: var(--navy); flex: none; }
  .contacts .city { padding-left: 30px; }
</style>
</head>
<body>
<main class="canvas">

  <section class="card card--back">
    <div class="kitchen-photo" role="img" aria-label="Photo of a bright kitchen with light wood cabinets, white island, bar stools and pendant lights"></div>
  </section>

  <section class="card card--front">
    <div class="portrait" role="img" aria-label="Portrait photo of the owner in a checked blazer and white shirt"></div>

    <div class="brand">
      <span class="brand-name">Willowmere<br>Kitchen &amp; Bath</span>
    </div>

    <div class="identity">
      <h1 class="person-name">Desmond Ferrick</h1>
      <p class="person-role">GC/Owner</p>
    </div>

    <ul class="contacts">
      <li>
        <svg viewBox="0 0 24 24" aria-hidden="true"><path d="M6.6 10.8a15 15 0 0 0 6.6 6.6l2.2-2.2c.3-.3.7-.4 1-.2 1.1.4 2.3.6 3.6.6.6 0 1 .4 1 1V20c0 .6-.4 1-1 1C10.6 21 3 13.4 3 4c0-.6.4-1 1-1h3.5c.6 0 1 .4 1 1 0 1.3.2 2.5.6 3.6.1.3 0 .7-.2 1z"/></svg>
        704-555-0183
      </li>
      <li>
        <svg viewBox="0 0 24 24" aria-hidden="true"><path d="M2 5h20v14H2zm2 2v.5l8 5 8-5V7l-8 5z"/></svg>
        desmond@willowmereKB.example
      </li>
      <li>
        <svg viewBox="0 0 24 24" aria-hidden="true"><path d="M12 2a10 10 0 1 0 0 20 10 10 0 0 0 0-20zm1 17.9V17h-2v2.9A8 8 0 0 1 4.1 13H7v-2H4.1A8 8 0 0 1 11 4.1V7h2V4.1A8 8 0 0 1 19.9 11H17v2h2.9A8 8 0 0 1 13 19.9z"/></svg>
        www.willowmereKB.example
      </li>
      <li class="city">Larkfield NC</li>
    </ul>

    <div class="tagline-band">
      BEAUTY<span class="sep">|</span>FUNCTION<span class="sep">|</span>ON TIME<span class="sep">|</span>ON BUDGET
    </div>
  </section>

</main>
</body>
</html>
```